Vacation giveaway landing page design

We are giving away a holiday/vacation to Rome and we need a landing page designed that will entice people to enter their email address for a chance to win!

Full brief, examples and everything else can be found in this document: https://files.brintowle.net/papers/p/4-wxkoppTR7mnbQ2vyLazcR5xsjfPe3lhmwcKt27r/view?mode=linked

1 page

```html
<!DOCTYPE html>
<html lang="en">
<head>
<meta charset="utf-8">
<title>The Wish Weavers – Monthly Prize Draw</title>
<link href="https://fonts.googleapis.com/css2?family=Fjalla+One&family=Archivo:wght@400;600;700;800&display=swap" rel="stylesheet">
<style>
:root{
  --teal:#36c2b4;
  --teal-dark:#1fa9a0;
  --blue-link:#2a7fd1;
  --ink:#222;
  --muted:#666;
  --white:#fff;
  --gold:#f5c242;
  --red:#f04c4c;
  --footer:#1c1d20;
  --footer-text:#e6e6e6;
  --line:#d9dde3;
  --quote-border:#6aa9cf;
  --quote-text:#1c86a8;
  --hero-top:#2b2f78;
  --hero-bottom:#4c4a98;
}
*{box-sizing:border-box;margin:0;padding:0}
html,body{width:852px;height:1200px;overflow:hidden;background:var(--white)}
body{position:relative;font-family:"Archivo",Arial,sans-serif;color:var(--ink)}
.abs{position:absolute}
.display{font-family:"Fjalla One","Arial Narrow",sans-serif}

/* hero */
.hero{left:0;top:0;width:852px;height:415px;background:linear-gradient(180deg,var(--hero-top) 0%,var(--hero-bottom) 100%)}
.brand{left:123px;top:16px;display:flex;align-items:center;gap:8px}
.brand-dot{width:30px;height:30px;border:2px solid var(--white);border-radius:50%}
.brand-name{font-family:"Fjalla One",sans-serif;color:var(--white);font-size:18px;line-height:1}
.prize-kicker{left:123px;top:119px;font-family:"Fjalla One",sans-serif;color:var(--teal);font-size:15px;letter-spacing:.5px}
.prize-detail{left:123px;color:var(--white);font-weight:700;font-size:16px}
.stars{color:var(--gold);letter-spacing:1px}
.prize-title{left:121px;top:176px;color:var(--white);font-size:69px;line-height:63px;letter-spacing:1px}

.countdown-title{left:513px;top:96px;width:217px;text-align:center;color:var(--white);font-weight:600;font-size:15.5px}
.countdown{left:513px;top:121px;width:217px;height:51px;border:1px solid rgba(255,255,255,.55);border-radius:8px;background:rgba(40,90,160,.35);display:flex;justify-content:space-around;align-items:center;color:var(--white)}
.unit{text-align:center}
.unit b{display:block;font-size:17px;font-weight:700;line-height:18px}
.unit span{font-size:8px}
.colon{font-weight:700;font-size:16px;margin-top:-12px}
.field{left:513px;width:217px;height:18px;border-bottom:1px solid rgba(255,255,255,.8);color:var(--white);font-size:7.5px;padding-left:10px}
.submit{left:513px;top:248px;width:217px;height:23px;background:var(--teal);color:var(--white);font-weight:700;font-size:8.5px;display:flex;align-items:center;justify-content:center}
.consent{left:513px;top:279px;width:217px;color:var(--white);font-size:7.3px;line-height:10px;padding-left:10px}
.consent i{position:absolute;left:0;top:2px;width:6px;height:6px;background:var(--white)}
.dots{left:819px;top:190px}
.dots i{display:block;width:8px;height:8px;border-radius:50%;margin-bottom:3px;background:#b9c4d4}
.dots i+i{background:var(--teal-dark)}

/* winners */
.section-title{left:0;top:480px;width:852px;text-align:center;color:var(--teal);font-size:19px;font-weight:800;letter-spacing:.2px}
.winner{width:141px}
.winner-kicker{color:var(--quote-text);font-size:7px;text-align:center;height:9px}
.winner-prize{color:var(--teal);font-weight:800;font-size:10.5px;line-height:13px;text-align:center;height:34px;padding-top:1px}
.post{border:1px solid var(--line);border-radius:3px;height:266px;background:var(--white);position:relative}
.post-photo{height:118px;position:relative}
.post-head{position:absolute;left:4px;top:4px;display:flex;gap:4px;color:var(--white)}
.post-head i{width:18px;height:18px;background:var(--white)}
.post-head b{font-size:7.5px;display:block}
.post-head span{font-size:6.5px}
.post-text{padding:5px 5px 0;font-size:7.7px;line-height:11.6px}
.post-text a{color:var(--blue-link);text-decoration:none}
.post-stats{position:absolute;left:5px;right:5px;bottom:6px;border-top:1px solid var(--line);padding-top:5px;font-size:6.5px;color:var(--muted);display:flex;gap:12px}
.quote{margin-top:19px;height:103px;border:1px solid var(--quote-border);position:relative;text-align:center;padding:8px 5px 0}
.quote::before{content:"";position:absolute;left:62px;top:-7px;width:12px;height:12px;background:var(--white);border-left:1px solid var(--quote-border);border-top:1px solid var(--quote-border);transform:rotate(45deg)}
.quote-mark{color:#9a9a9a;font-family:Georgia,serif;font-size:38px;line-height:26px;font-weight:700}
.quote p{color:var(--quote-text);font-weight:700;font-size:9px;line-height:12.5px;letter-spacing:-.2px;margin-top:6px}

.join{left:279px;top:1011px;width:295px;height:26px;background:var(--red);color:var(--white);font-weight:700;font-size:10.5px;display:flex;align-items:center;justify-content:center}

/* footer */
.footer{left:0;top:1073px;width:852px;height:127px;background:var(--footer);color:var(--footer-text)}
.contact{top:32px;display:flex;align-items:center;gap:8px;font-size:8.5px}
.social{left:381px;top:63px;display:flex;gap:3px}
.social i{width:20px;height:21px}
.rule{left:118px;top:96px;width:616px;height:1px;background:#3a3b40}
.legal{left:118px;top:108px;width:616px;font-size:6.6px;display:flex;align-items:center;gap:10px}
.cards{margin-left:auto;display:flex;gap:2px}
.cards i{width:12px;height:7px;background:#d8d8d8;border-radius:1px}
</style>
</head>
<body>

<section class="hero abs" role="img" aria-label="Photograph of the northern lights over a snowy forest landscape"></section>

<div class="brand abs"><span class="brand-dot"></span><span class="brand-name">The Wish Weavers</span></div>

<p class="prize-kicker abs">THIS MONTH'S PRIZE</p>
<p class="prize-detail abs" style="top:139px">4 Nights, 2 People</p>
<p class="prize-detail abs" style="top:157px">Flights + Hotel <span class="stars">★★★★★</span></p>
<h1 class="prize-title display abs">NORTHERN<br>LIGHTS</h1>

<p class="countdown-title abs">Hurry! Prize draw closes in</p>
<div class="countdown abs">
  <div class="unit"><b>04</b><span>Days</span></div><span class="colon">:</span>
  <div class="unit"><b>06</b><span>Hours</span></div><span class="colon">:</span>
  <div class="unit"><b>22</b><span>Minutes</span></div><span class="colon">:</span>
  <div class="unit"><b>24</b><span>Seconds</span></div>
</div>
<div class="field abs" style="top:191px">Your Name</div>
<div class="field abs" style="top:224px">Email address</div>
<div class="submit abs">SUBMIT</div>
<p class="consent abs"><i></i>By entering your email address, you agree to receive updates about the competition and The Wish Weavers. You can review our competition terms and conditions here</p>
<div class="dots abs"><i></i><i></i></div>

<h2 class="section-title abs">OUR PREVIOUS WINNERS</h2>

<article class="winner abs" style="left:122px;top:526px">
  <p class="winner-kicker">SEPTEMBER'S WINNER PRIZE</p>
  <p class="winner-prize">A WEEK IN PORTUGAL</p>
  <div class="post">
    <div class="post-photo" role="img" aria-label="Photo of the winner standing in a green mountain valley" style="background:linear-gradient(180deg,#8a9aa8,#5d6b4a)">
      <div class="post-head"><i></i><div><b>The Wish Weavers</b><span>about 9 months ago</span></div></div>
    </div>
    <p class="post-text">🎉 Our Lucky winner of this month's prize draw is... Clara-Jane Holt! 🎉 A HUGE congratulations to her as she's jetting off to the Algarve in Portugal for an incredible week in the sun!<br>Next month's giveaway is a trip to the Canary Islands - find out more here: <a>https://go.example/2Kx4pQ1</a></p>
    <div class="post-stats"><span>👍 21</span><span>💬 5</span><span>➦ 1</span></div>
  </div>
  <div class="quote"><div class="quote-mark">“</div><p>Lorem ipsum dolor sit amet, consectetur adipiscing elit, sed do eiusmod tempor incididunt</p></div>
</article>

<article class="winner abs" style="left:278px;top:526px">
  <p class="winner-kicker">DECEMBER'S WINNER PRIZE</p>
  <p class="winner-prize">A HOLIDAY IN VALENCIA, SPAIN</p>
  <div class="post">
    <div class="post-photo" role="img" aria-label="Photo of the winner in a warmly lit room" style="background:linear-gradient(180deg,#5a2a3a,#c9a58a)">
      <div class="post-head"><i></i><div><b>The Wish Weavers</b><span>about 6 months ago</span></div></div>
    </div>
    <p class="post-text">Looks like Sophie is the lucky one this month as she's won a trip to Valencia! What a Christmas present!<br>Want something to look forward to in the New Year? You could win a trip to see the Northern Lights by signing up here - <a>https://go.example/2Kx4pQ1</a></p>
    <div class="post-stats"><span>👍 18</span><span>💬 Comment</span><span>➦ 2</span></div>
  </div>
  <div class="quote"><div class="quote-mark">“</div><p>Lorem ipsum dolor sit amet, consectetur adipiscing elit, sed do eiusmod tempor incididunt</p></div>
</article>

<article class="winner abs" style="left:434px;top:526px">
  <p class="winner-kicker">OCTOBER'S WINNER PRIZE</p>
  <p class="winner-prize">A WEEK IN THE CANARY ISLANDS</p>
  <div class="post">
    <div class="post-photo" role="img" aria-label="Photo of the winner outdoors beside a river" style="background:linear-gradient(180deg,#8fa7b8,#6a7a5a)">
      <div class="post-head"><i></i><div><b>The Wish Weavers</b><span>about 8 months ago</span></div></div>
    </div>
    <p class="post-text">This month's winner is just too kind 😊 Ravi Mehta won a trip to the Canary Islands but has decided to give the prize to his parents who have always wanted to go. Congrats to Ravi and his parents!<br>Feeling lucky? Click here for your chance to win a trip to Valencia - <a>http://go.example/7hbtw</a></p>
    <div class="post-stats"><span>👍 15</span><span>💬 3</span><span>➦ 1</span></div>
  </div>
  <div class="quote"><div class="quote-mark">“</div><p>Lorem ipsum dolor sit amet, consectetur adipiscing elit, sed do eiusmod tempor incididunt</p></div>
</article>

<article class="winner abs" style="left:590px;top:526px">
  <p class="winner-kicker">APRIL'S WINNER PRIZE</p>
  <p class="winner-prize">A WEEK IN PORTUGAL</p>
  <div class="post">
    <div class="post-photo" role="img" aria-label="Photo of the winner in a sunny park" style="background:linear-gradient(180deg,#6a8a4a,#5a7a3a)">
      <div class="post-head"><i></i><div><b>The Wish Weavers</b><span>about 2 months ago</span></div></div>
    </div>
    <p class="post-text">🎉 Congratulations to this month's winner Tina Marlow - she has won a week long holiday in B-E-A-UTIFUL 🇵🇹 Portugal! 🇵🇹<br>Next month you could win 7 nights in the Canary Islands! Get signed up here -<a>http://go.example/3Rmc9Lz</a></p>
    <div class="post-stats"><span>👍 17</span><span>💬 3</span><span>➦ 2</span></div>
  </div>
  <div class="quote"><div class="quote-mark">“</div><p>Lorem ipsum dolor sit amet, consectetur adipiscing elit, sed do eiusmod tempor incididunt</p></div>
</article>

<div class="join abs">WHAT ARE YOU WAITING FOR? JOIN NOW!</div>

<footer class="footer abs">
  <div class="contact abs" style="left:126px">
    <svg width="10" height="13" viewBox="0 0 10 13" fill="none" stroke="#2a9fd6" stroke-width="1.3"><path d="M5 12S1 7.5 1 5a4 4 0 0 1 8 0c0 2.5-4 7-4 7z"/><circle cx="5" cy="5" r="1.4"/></svg>
    <span>42 Harbour Lane, London, SE1 4XY, UK</span>
  </div>
  <div class="contact abs" style="left:372px">
    <svg width="12" height="12" viewBox="0 0 12 12" fill="none" stroke="#2a9fd6" stroke-width="1.2"><path d="M2 1h2.5l1 3-1.5 1a7 7 0 0 0 3 3l1-1.5 3 1V10a1 1 0 0 1-1 1A10 10 0 0 1 1 2a1 1 0 0 1 1-1z"/></svg>
    <span>+44 (0) 203 555 0142</span>
  </div>
  <div class="contact abs" style="left:562px">
    <svg width="13" height="10" viewBox="0 0 13 10" fill="none" stroke="#2a9fd6" stroke-width="1.2"><rect x=".6" y=".6" width="11.8" height="8.8" rx="1"/><path d="M.8 1l5.7 4.5L12.2 1"/></svg>
    <span>hello@wishweavers.example</span>
  </div>
  <div class="social abs">
    <i style="background:#3b5bab"></i><i style="background:#2aa3e0"></i><i style="background:#8a5a44"></i><i style="background:#d92a2a"></i>
  </div>
  <div class="rule abs"></div>
  <div class="legal abs">
    <span>© 2019 Northwind Holdings LTD a private limited company registered in England and Wales, Reg No: 12345678.</span>
    <span>|</span><span>Terms &amp; Conditions</span><span>|</span><span>Privacy Policy</span>
    <span class="cards"><i></i><i></i><i></i><i></i><i></i></span>
  </div>
</footer>

</body>
</html>
```